Website Design for Halden Streamcut - Specialised Waterjet Cutting Service Provider

Description:
We are seeking a talented and creative web designer to create a new, single-page scrolling website for our company, Halden Streamcut. We specialise in providing waterjet cutting services, with over 15 years of experience in the industry and a strong focus on serving the film and TV sector. Our goal is to showcase our expertise, services, and dedication to delivering exceptional quality and timely project completion.
Design Requirements:
Use existing website as a template: Please use our current website (www.haldenstreamcut-example.com) as a template for the new design. We would like the new website to maintain a similar structure and feel, but with a refreshed and modernised appearance.
Single-page scrolling website: Design a single-page scrolling website with clear, intuitive navigation for each section.
Professional and modern design: The website should have a clean, professional, and modern aesthetic that appeals to both film industry professionals and other potential clients seeking waterjet cutting services.
Responsive design: The website must be fully responsive and compatible with various devices, including desktop computers, laptops, tablets, and smartphones.
Colour scheme: We prefer a colour scheme that includes shades of blue, grey, and white. However, we are open to creative suggestions that align with our brand identity and industry.
Typography: The font choice should be clean, legible, and professional.
Imagery: The website should incorporate high-quality images showcasing our waterjet cutting services, machinery, and examples of completed projects.
Integration of Plover Ratings: The website design should incorporate a section or widget that displays our Plover Ratings, highlighting our customers' positive experiences and showcasing our commitment to quality service.
Contact Information: Instead of a contact form, please include our email address and telephone number on the site, accompanied by a friendly message encouraging visitors to get in touch with us for any inquiries.
Industries Served: While our primary focus is the film and TV industry, please highlight that we also cater to aerospace, motorsport, engineering projects, oil and gas, pharmaceutical, space, fusion energy, and EV projects. Also, mention that we have worked with several ClipNest creators.
Fastest Turnaround Time: Emphasise that we have the fastest turnaround time for waterjet cutting services in the south of the UK.
Friendly and Creative Team: Emphasise that we are a friendly team who enjoy working with creative individuals, fostering a collaborative and enjoyable working environment for all parties involved.
Proposed Website Sections:
Home
About Us
Services
Portfolio
Testimonials
Contact Us
Please provide initial design concepts for the single-page scrolling website, keeping in mind the similarity to our existing website. We look forward to reviewing your creative proposals and working with you to create a website that effectively represents our brand and appeals to our target audience while maintaining the essence of our current website.
Target Market(s)
Film Industry

```html
<!DOCTYPE html>
<html lang="en">
<head>
<meta charset="utf-8">
<title>Halden Streamcut – Waterjet Cutting</title>
<link rel="stylesheet" href="https://fonts.googleapis.com/css2?family=Orbitron:wght@700;800;900&family=Poppins:wght@400;500;600&display=swap">
<style>
:root{
  --ink:#222222;
  --dark:#2e2e2e;
  --blue:#1a6190;
  --blue-light:#2572a6;
  --nav-blue:#3d6f9c;
  --white:#ffffff;
  --grey:#a9a9a9;
  --star:#f2c31b;
}
*{box-sizing:border-box;margin:0;padding:0}
html,body{width:1200px;height:4587px;overflow:hidden}
body{position:relative;background:var(--white);font-family:"Poppins",sans-serif;color:var(--ink)}
.abs{position:absolute}
.display{font-family:"Orbitron",sans-serif;font-weight:800;letter-spacing:1px;text-transform:uppercase}

/* header */
.site-header{left:0;top:0;width:1200px;height:71px;background:var(--white)}
.brand{display:flex;align-items:center;gap:10px;color:var(--blue);font-family:"Poppins",sans-serif;font-weight:600;font-size:20px;white-space:nowrap}
.brand-mark{width:14px;height:14px;background:var(--blue);border-radius:50%}
.site-header .brand{position:absolute;left:101px;top:22px}
.main-nav a{position:absolute;top:25px;font-size:15px;color:var(--nav-blue);text-decoration:none}

/* hero */
.hero{left:0;top:71px;width:1200px;height:668px;overflow:hidden}
.hero-photo{position:absolute;inset:0;background:linear-gradient(100deg,#6d7aa0 0%,#8aa1c6 30%,#b7c7df 55%,#8d7a5e 75%,#c9d6e8 100%)}
.hero-box{left:68px;top:121px;width:719px;height:388px;background:rgba(62,62,62,.88);padding:22px 32px}
.hero-box .line{color:var(--white);font-size:41px;line-height:71px;height:71px;letter-spacing:1.5px;white-space:nowrap}
.line.center{text-align:center}
.line.spread{display:flex;justify-content:space-between}
.hero-arrow{width:22px;height:22px;border:1.5px solid rgba(255,255,255,.7);border-radius:50%}
.hero-edge{left:0;bottom:0;width:1200px;height:110px}

/* about */
.about-photo{clip-path:polygon(0 0,100% 0,100% 68%,50% 100%,0 68%)}
.about-title{left:712px;top:836px;font-size:40px;color:var(--ink)}
.about-text{left:575px;top:944px;width:513px;font-size:16.5px;line-height:30px;color:#333;text-align:justify}
.about-text p+p{margin-top:30px}

/* services */
.services{left:0;top:1489px;width:1200px;height:705px;background:var(--dark)}
.services-title{left:178px;top:1686px;font-size:42px;color:var(--white)}
.service-card{width:397px;height:205px;border:3px solid var(--white);color:var(--white)}
.service-card h3{position:absolute;left:144px;top:24px;font-family:"Poppins",sans-serif;font-weight:600;font-size:15px;text-transform:uppercase;letter-spacing:.3px;white-space:nowrap}
.service-card p{position:absolute;left:24px;right:24px;top:80px;font-size:14px;line-height:29px;text-align:center;text-transform:uppercase}
.service-card p.plain{text-transform:none;font-size:15px}
.service-icon{position:absolute;left:32px;top:-46px;width:101px;height:100px;background:var(--white);display:flex;align-items:center;justify-content:center}
.notch{position:absolute;left:50%;bottom:-15px;margin-left:-16px;width:32px;height:16px}

/* portfolio */
.portfolio{left:0;top:2194px;width:1200px;height:757px;background:var(--blue)}
.portfolio-title{left:0;width:1200px;top:2288px;text-align:center;font-size:38px;color:var(--white)}
.tile{width:319px;height:216px}
.circle-arrow{width:22px;height:22px}

/* testimonials */
.testimonials-title{left:0;width:1200px;top:3056px;text-align:center;font-size:38px;color:var(--ink)}
.review{background:var(--white)}
.review.side{opacity:.35;box-shadow:0 2px 10px rgba(0,0,0,.12)}
.review.main{box-shadow:0 4px 22px rgba(0,0,0,.16)}
.stars{color:var(--star);letter-spacing:2px}
.avatar{border-radius:50%}
.review-name{font-family:"Orbitron",sans-serif;font-weight:700;text-transform:uppercase;white-space:nowrap}
.dots span{display:inline-block;width:7px;height:7px;border-radius:50%;background:#9a9a9a;margin:0 1px}

/* industries */
.industries{left:0;top:3512px;width:1200px;height:771px;background:var(--dark)}
.industries-title{left:0;width:1200px;top:3617px;text-align:center;font-size:40px;color:var(--white)}
.ind-label{color:var(--white);font-family:"Poppins",sans-serif;font-weight:500;font-size:16px;text-transform:uppercase;text-align:center;line-height:22px}
.hex-down{clip-path:polygon(0 0,100% 0,100% 72%,72% 100%,28% 100%,0 72%)}
.hex-up{clip-path:polygon(28% 0,72% 0,100% 28%,100% 100%,0 100%,0 28%)}
.dark-dots span{background:#c8c8c8}

/* footer */
.site-footer{left:0;top:4283px;width:1200px;height:304px;background:var(--blue)}
.footer-nav{left:468px;top:4283px;width:732px;height:50px;background:var(--blue-light)}
.footer-nav a{position:absolute;top:14px;color:var(--white);font-size:15px;text-decoration:none}
.footer-brand{left:101px;top:4283px;width:367px;height:258px;background:var(--white)}
.footer-brand .brand{position:absolute;left:85px;top:52px}
.footer-tagline{position:absolute;left:50px;right:50px;top:122px;font-family:"Orbitron",sans-serif;font-weight:700;font-size:14px;line-height:21px;text-align:center;text-transform:uppercase;color:var(--ink)}
.footer-text{color:var(--white);font-size:16px;line-height:29px}
.footer-contact{white-space:nowrap;text-align:right}
.social{width:17px;height:17px;border:2px solid var(--white);border-radius:3px}
.copyright{left:0;width:1200px;top:4552px;text-align:center;color:var(--white);font-size:13px}
</style>
</head>
<body>

<header class="abs site-header">
  <div class="brand"><span class="brand-mark"></span>Halden Streamcut</div>
  <nav class="main-nav">
    <a href="#home" style="left:442px">Home</a>
    <a href="#about" style="left:541px">About Us</a>
    <a href="#services" style="left:655px">Services</a>
    <a href="#portfolio" style="left:764px">Portfolio</a>
    <a href="#testimonials" style="left:889px">Testimonial</a>
    <a href="#contact" style="left:1023px">contact</a>
  </nav>
</header>

<section class="abs hero" id="home">
  <div class="hero-photo" role="img" aria-label="Waterjet cutting head spraying onto a water table"></div>
  <div class="abs hero-box display">
    <div class="line center">We have the fastest</div>
    <div class="line spread"><span>Turnaround</span><span>time</span><span>for</span></div>
    <div class="line center">Waterjet cutting</div>
    <div class="line spread"><span>Services</span><span>in</span><span>the</span><span>south</span></div>
    <div class="line center">of the UK</div>
  </div>
  <div class="abs hero-arrow" style="left:34px;top:288px"></div>
  <div class="abs hero-arrow" style="left:1146px;top:288px"></div>
  <svg class="abs hero-edge" viewBox="0 0 1200 110" preserveAspectRatio="none">
    <path d="M0 0 Q300 80 600 110 L0 110Z" fill="#a7a7a7"/>
    <path d="M600 110 Q900 70 1200 -10 L1200 110Z" fill="#a7a7a7"/>
    <path d="M0 18 Q300 95 600 110 Q900 78 1200 8 L1200 110 L0 110Z" fill="#ffffff"/>
  </svg>
</section>

<section id="about">
  <div class="abs about-photo" style="left:18px;top:810px;width:343px;height:330px;background:linear-gradient(135deg,#cfd6dc,#8c99a5 60%,#4f6474)" role="img" aria-label="Operator working at a waterjet control console"></div>
  <div class="abs" style="left:164px;top:988px;width:343px;height:419px;filter:drop-shadow(0 6px 10px rgba(0,0,0,.3))">
    <div class="about-photo" style="width:343px;height:419px;background:linear-gradient(160deg,#3b3b3b 0%,#9ea3a8 40%,#c9cdd1 100%)" role="img" aria-label="Cutting head tracing a shape on a metal sheet"></div>
  </div>
  <h2 class="abs about-title display">About us</h2>
  <div class="abs about-text">
    <p>Halden Streamcut has been providing a profile cutting service primarily to the film industry for over 15 years. We are used to working within tight timeframes with a fast turnaround for all aspects of Water Jet Profiling, Abrasive Steel Cutting and Foam-Water Jet Cutting.</p>
    <p>By combining our technical expertise with Veyra’s latest dynamic head waterjet technology we are able to offer a Profiling Services which can be tailored to each individual client and completed within fine tolerances to precise specifications. We are happy to cut your material or where required we can source most materials to your requirement</p>
  </div>
</section>

<section class="abs services" id="services"></section>
<h2 class="abs services-title display">Our services</h2>

<article class="abs service-card" style="left:648px;top:1606px">
  <div class="service-icon">
    <svg width="64" height="64" viewBox="0 0 64 64"><path d="M14 6h36v10L36 30v10h-8V30L14 16z" fill="#3a3a3a"/><path d="M32 42v10" stroke="#3a3a3a" stroke-width="3"/><path d="M20 58h24M24 50l-6 6M40 50l6 6" stroke="#3a3a3a" stroke-width="2"/></svg>
  </div>
  <h3>Blank preparation</h3>
  <p>Lorem ipsum dolor sit amet, consectetur adipiscing elit, sed ut labore et dolore magna aliqua. Ut enim ad minim veniam</p>
  <svg class="notch" viewBox="0 0 32 16"><path d="M0 0 L16 16 L32 0" fill="#2e2e2e" stroke="#fff" stroke-width="3"/></svg>
</article>

<article class="abs service-card" style="left:164px;top:1909px">
  <div class="service-icon">
    <svg width="64" height="64" viewBox="0 0 64 64"><circle cx="32" cy="32" r="24" fill="none" stroke="#3a3a3a" stroke-width="3"/><circle cx="32" cy="32" r="13" fill="#3a3a3a"/><path d="M20 54 l12 -8 12 8" fill="#3a3a3a"/></svg>
  </div>
  <h3>End-use production</h3>
  <p>Lorem ipsum dolor sit amet, consectetur adipiscing elit, sed ut labore et dolore magna aliqua. Ut enim ad minim veniam</p>
  <svg class="notch" viewBox="0 0 32 16"><path d="M0 0 L16 16 L32 0" fill="#2e2e2e" stroke="#fff" stroke-width="3"/></svg>
</article>

<article class="abs service-card" style="left:648px;top:1909px">
  <div class="service-icon">
    <svg width="64" height="64" viewBox="0 0 64 64"><circle cx="32" cy="16" r="8" fill="none" stroke="#3a3a3a" stroke-width="3"/><rect x="8" y="32" width="48" height="12" rx="6" fill="none" stroke="#3a3a3a" stroke-width="3"/><circle cx="18" cy="38" r="3" fill="#3a3a3a"/><circle cx="32" cy="38" r="3" fill="#3a3a3a"/><circle cx="46" cy="38" r="3" fill="#3a3a3a"/><path d="M16 50v8M32 50v8M48 50v8" stroke="#3a3a3a" stroke-width="2"/></svg>
  </div>
  <h3>Rapid prototyping</h3>
  <p class="plain">Lorem ipsum dolor sit amet, consectetur adipiscing elit, sed ut labore et dolore magna aliqua. Ut enim ad minim veniam</p>
  <svg class="notch" viewBox="0 0 32 16"><path d="M0 0 L16 16 L32 0" fill="#2e2e2e" stroke="#fff" stroke-width="3"/></svg>
</article>

<section class="abs portfolio" id="portfolio"></section>
<h2 class="abs portfolio-title display">Our portfolio</h2>
<div class="abs tile" style="left:98px;top:2400px;background:linear-gradient(135deg,#8c958f,#b9bcb6 50%,#6e7b78)" role="img" aria-label="Waterjet nozzle above a cut plate"></div>
<div class="abs tile" style="left:431px;top:2400px;background:linear-gradient(135deg,#5e5e5e,#b5b5b5 50%,#4a4a4a)" role="img" aria-label="Pile of waterjet-cut metal letters"></div>
<div class="abs tile" style="left:762px;top:2400px;background:linear-gradient(135deg,#e6e8ea,#8d9aa4 55%,#5a6f82)" role="img" aria-label="Technician at the machine controls"></div>
<div class="abs tile" style="left:98px;top:2630px;background:linear-gradient(135deg,#7b7b7b,#3c3c3c 50%,#9a9a9a)" role="img" aria-label="Waterjet machine bed with slats"></div>
<div class="abs tile" style="left:431px;top:2630px;background:linear-gradient(135deg,#0c2b6b,#2c7fd6 55%,#7bc4ff)" role="img" aria-label="Cutting head in blue water spray"></div>
<div class="abs tile" style="left:762px;top:2630px;background:linear-gradient(135deg,#2e2a25,#7a746c 50%,#3b3833)" role="img" aria-label="Close-up of a polished cut metal edge"></div>
<svg class="abs circle-arrow" style="left:34px;top:2614px" viewBox="0 0 22 22"><circle cx="11" cy="11" r="10" fill="none" stroke="#cfe0ee" stroke-width="1.3"/><path d="M13 6l-5 5 5 5" fill="none" stroke="#cfe0ee" stroke-width="1.3"/></svg>
<svg class="abs circle-arrow" style="left:1145px;top:2614px" viewBox="0 0 22 22"><circle cx="11" cy="11" r="10" fill="none" stroke="#cfe0ee" stroke-width="1.3"/><path d="M9 6l5 5-5 5" fill="none" stroke="#cfe0ee" stroke-width="1.3"/></svg>

<section id="testimonials">
  <h2 class="abs testimonials-title display">Testimonials</h2>

  <div class="abs review side" style="left:105px;top:3216px;width:230px;height:189px">
    <div class="stars" style="position:absolute;left:160px;top:14px;font-size:15px">★★★★</div>
    <p style="position:absolute;left:46px;top:42px;width:180px;font-size:11px;line-height:22px;color:#777">Lorem ipsum dolor sit amet, co sed do eiusmod tempor incid magna aliqua. Ut enim ad minim</p>
    <div class="avatar" style="position:absolute;left:26px;top:120px;width:52px;height:52px;background:#d9c3b4" role="img" aria-label="Reviewer portrait"></div>
    <div class="review-name" style="position:absolute;left:104px;top:139px;font-size:11px;color:#777">Rowan</div>
  </div>

  <div class="abs review side" style="left:862px;top:3216px;width:219px;height:189px">
    <div class="stars" style="position:absolute;left:0;top:14px;font-size:15px">★★★★</div>
    <p style="position:absolute;left:0;top:42px;width:170px;font-size:11px;line-height:22px;color:#777">amet, consectetur adipiscing elit, tempor incididunt ut labore et dolore</p>
    <div class="review-name" style="position:absolute;left:28px;top:139px;font-size:11px;color:#777">Callum Reyes</div>
    <div class="avatar" style="position:absolute;left:140px;top:120px;width:52px;height:52px;background:#b9b2ad" role="img" aria-label="Reviewer portrait"></div>
  </div>

  <div class="abs review main" style="left:317px;top:3177px;width:545px;height:260px">
    <div class="stars" style="position:absolute;left:0;width:545px;top:16px;text-align:center;font-size:22px">★★★★★</div>
    <p style="position:absolute;left:40px;right:40px;top:54px;font-size:15.5px;line-height:30px;text-align:center;color:#333">Lorem ipsum dolor sit amet, consectetur adipiscing elit, sed do eiusmod tempor incididunt ut labore et dolore magna aliqua. Ut enim ad minim veniam, quis nostrud ex-</p>
    <div class="avatar" style="position:absolute;left:36px;top:156px;width:76px;height:76px;background:#c98f70" role="img" aria-label="Reviewer portrait"></div>
    <div class="review-name" style="position:absolute;left:142px;top:184px;font-size:15px;font-family:'Poppins',sans-serif;font-weight:500;color:#333">Martin</div>
    <div style="position:absolute;right:36px;top:182px;font-size:14px;font-weight:600;color:var(--blue)">Plover</div>
  </div>

  <div class="abs dots" style="left:0;width:1200px;top:3481px;text-align:center"><span></span><span></span><span></span></div>
</section>

<section class="abs industries"></section>
<h2 class="abs industries-title display">Industries served</h2>
<div class="abs ind-label" style="left:105px;width:239px;top:3716px">Film</div>
<div class="abs ind-label" style="left:356px;width:237px;top:3716px">TV industry</div>
<div class="abs ind-label" style="left:605px;width:237px;top:3716px">Aerospace</div>
<div class="abs ind-label" style="left:855px;width:250px;top:3716px">Motorsport</div>

<div class="abs hex-down" style="left:105px;top:3752px;width:239px;height:210px;background:radial-gradient(circle at 70% 40%,#c58b4a,#3a2a1c 55%,#111)" role="img" aria-label="Vintage film projector"></div>
<div class="abs hex-down" style="left:356px;top:3752px;width:237px;height:210px;background:linear-gradient(160deg,#4a4f57,#b57a3e 60%,#2b2b2b)" role="img" aria-label="TV studio camera rig"></div>
<div class="abs hex-down" style="left:605px;top:3752px;width:237px;height:210px;background:linear-gradient(160deg,#d9e2ea,#9aa8b4 55%,#e9eef2)" role="img" aria-label="Jet engine on an aircraft wing"></div>
<div class="abs hex-down" style="left:855px;top:3752px;width:238px;height:210px;background:linear-gradient(160deg,#7a4b2a,#1d1d1d 55%,#a13328)" role="img" aria-label="Racing car on track"></div>

<div class="abs hex-up" style="left:226px;top:3909px;width:239px;height:210px;background:linear-gradient(160deg,#2b3347,#6b7890 55%,#c7a35a)" role="img" aria-label="Engineering gears and machinery"></div>
<div class="abs hex-up" style="left:474px;top:3909px;width:238px;height:210px;background:linear-gradient(180deg,#2f4f6e,#e0a45b 55%,#3a3b40)" role="img" aria-label="Offshore oil platform at sunset"></div>
<div class="abs hex-up" style="left:723px;top:3909px;width:239px;height:210px;background:linear-gradient(160deg,#4f9fd8,#1c5fa0 55%,#d8e7f5)" role="img" aria-label="Capsules and pills on blue"></div>

<div class="abs ind-label" style="left:226px;width:239px;top:4134px">Engineering<br>projects</div>
<div class="abs ind-label" style="left:474px;width:238px;top:4138px">Oil and gas</div>
<div class="abs ind-label" style="left:723px;width:239px;top:4140px">Pharmaceutica</div>
<div class="abs dots dark-dots" style="left:0;width:1200px;top:4248px;text-align:center"><span></span><span></span><span></span></div>

<footer id="contact">
  <div class="abs site-footer"></div>
  <nav class="abs footer-nav">
    <a href="#home" style="left:20px">Home</a>
    <a href="#about" style="left:119px">About Us</a>
    <a href="#services" style="left:233px">Services</a>
    <a href="#portfolio" style="left:342px">Portfolio</a>
    <a href="#testimonials" style="left:466px">Testimonial</a>
    <span class="abs social" style="left:625px;top:16px"></span>
    <span class="abs social" style="left:654px;top:16px"></span>
    <span class="abs social" style="left:683px;top:16px"></span>
  </nav>
  <div class="abs footer-brand">
    <div class="brand"><span class="brand-mark"></span>Halden Streamcut</div>
    <p class="footer-tagline">We have the fastest turnaround time for waterjet cutting services in the south of the UK</p>
  </div>
  <address class="abs footer-text" style="left:516px;top:4380px;width:270px;font-style:normal">Unit 7, Harbour Court, Fenwick Road, Ashby Trade Park, Little Marlow, Bucks, HX9 4QT</address>
  <svg class="abs" style="left:1058px;top:4358px" width="22" height="16" viewBox="0 0 22 16"><rect x="1" y="1" width="20" height="14" fill="#e8493f"/><path d="M1 1l10 8 10-8" fill="none" stroke="#fff" stroke-width="2"/></svg>
  <div class="abs footer-text footer-contact" style="left:736px;width:350px;top:4388px">info@haldenstreamcut-example.com</div>
  <svg class="abs" style="left:1063px;top:4434px" width="18" height="18" viewBox="0 0 24 24"><path d="M6.6 10.8a15 15 0 006.6 6.6l2.2-2.2a1 1 0 011-.25 11 11 0 003.6.6 1 1 0 011 1V20a1 1 0 01-1 1A17 17 0 013 4a1 1 0 011-1h3.5a1 1 0 011 1 11 11 0 00.6 3.6 1 1 0 01-.25 1z" fill="#fff"/></svg>
  <div class="abs footer-text footer-contact" style="left:900px;width:186px;top:4460px">01632 960418</div>
  <div class="abs copyright">Copyright 2023 Halden Streamcut. All Rights Reserved.</div>
</footer>

</body>
</html>
```